Bref créative
Stationary for Stonebrook Putting Institute
Driving range/Golf Academy
Simple
Pieter de Groenhout
Director of Golfschool
P.O. Box 48306
00452 Nairobi
pieter@stonebrookputt.co.ke
www.stonebrookputt.com
I am a TCA Professional from Holland and the logo off the TCA Holland should be incorporated at the business card. You can download it from the internet.
We have 2 other people who need business cards, Wilhelmina Drostraat CEO
Tom Wanjau Director
These two no TCA LOGO
Business card with black back ground, and for Pieter de Groenhout inclusive TCA Holland logo,
Letterhead the white background

```html
<!DOCTYPE html>
<html lang="en">
<head>
<meta charset="utf-8">
<title>Stonebrook Putting Institute – Business Card</title>
<link rel="stylesheet" href="https://fonts.googleapis.com/css2?family=Open+Sans:wght@400;600;700&display=swap">
<style>
  :root {
    --stage: #34302e;
    --card-black: #0d0d0d;
    --card-charcoal: #242424;
    --brand-red: #c8141b;
    --brand-red-dark: #7d0a0e;
    --silver: #c9c9c9;
    --text-white: #ffffff;
    --text-grey: #bdbdbd;
    --web-grey: #9a9a9a;
  }
  html, body {
    margin: 0;
    padding: 0;
    width: 1200px;
    height: 901px;
    overflow: hidden;
    background: var(--stage);
  }
  .canvas {
    position: relative;
    width: 1200px;
    height: 901px;
  }
  .card {
    position: absolute;
    width: 600px;
    height: 343px;
    filter: drop-shadow(0 14px 22px rgba(0,0,0,0.55));
  }
  .card--back  { left: 60px;  top: 90px; }
  .card--front { left: 540px; top: 468px; }
  .card svg { display: block; width: 600px; height: 343px; }

  .wordmark {
    font-family: "Open Sans", Arial, sans-serif;
    font-weight: 700;
    fill: var(--text-white);
  }
  .person-name {
    font-family: "Open Sans", Arial, sans-serif;
    font-weight: 700;
    font-size: 17px;
    fill: var(--text-white);
  }
  .person-title {
    font-family: "Open Sans", Arial, sans-serif;
    font-weight: 400;
    font-size: 11px;
    fill: var(--text-white);
  }
  .address {
    font-family: "Open Sans", Arial, sans-serif;
    font-weight: 400;
    font-size: 12.5px;
    fill: var(--text-grey);
  }
  .contact-label {
    font-weight: 700;
    fill: var(--brand-red);
  }
  .website {
    font-family: "Open Sans", Arial, sans-serif;
    font-weight: 400;
    font-size: 12px;
    letter-spacing: 3px;
    fill: var(--web-grey);
  }
</style>
</head>
<body>
<main class="canvas">

  <!-- Back of card -->
  <section class="card card--back" aria-label="Business card, back">
    <svg viewBox="0 0 600 343" xmlns="http://www.w3.org/2000/svg">
      <defs>
        <linearGradient id="backFill" x1="0" y1="0" x2="1" y2="1">
          <stop offset="0" stop-color="var(--card-charcoal)"/>
          <stop offset="0.55" stop-color="var(--card-black)"/>
          <stop offset="1" stop-color="#161616"/>
        </linearGradient>
      </defs>
      <rect class="card-surface" width="600" height="343" rx="26" fill="url(#backFill)"/>
      <g class="brand-lockup">
        <circle cx="388" cy="167" r="9" fill="var(--brand-red)"/>
        <text class="wordmark" x="404" y="166" font-size="24">Stonebrook</text>
        <text class="wordmark" x="405" y="184" font-size="10.5">Putting Institute</text>
      </g>
    </svg>
  </section>

  <!-- Front of card -->
  <section class="card card--front" aria-label="Business card, front">
    <svg viewBox="0 0 600 343" xmlns="http://www.w3.org/2000/svg">
      <defs>
        <linearGradient id="frontFill" x1="0" y1="0" x2="1" y2="1">
          <stop offset="0" stop-color="var(--card-charcoal)"/>
          <stop offset="0.6" stop-color="var(--card-black)"/>
          <stop offset="1" stop-color="#141414"/>
        </linearGradient>
        <linearGradient id="redBand" x1="0" y1="0" x2="1" y2="1">
          <stop offset="0" stop-color="var(--brand-red)"/>
          <stop offset="1" stop-color="var(--brand-red-dark)"/>
        </linearGradient>
        <linearGradient id="silverBand" x1="0" y1="0" x2="1" y2="0">
          <stop offset="0" stop-color="#6e6e6e"/>
          <stop offset="0.5" stop-color="var(--silver)"/>
          <stop offset="1" stop-color="#8a8a8a"/>
        </linearGradient>
        <clipPath id="frontClip">
          <rect width="600" height="343" rx="26"/>
        </clipPath>
      </defs>

      <g clip-path="url(#frontClip)">
        <rect class="card-surface" width="600" height="343" fill="url(#frontFill)"/>
        <path class="silver-swoosh" fill="url(#silverBand)"
              d="M120 224 C 300 168 470 178 600 222 L 600 240 C 470 196 300 188 120 224 Z"/>
        <path class="red-band" fill="url(#redBand)"
              d="M210 0 L 600 0 L 600 214 C 470 172 300 162 128 216 C 210 160 240 80 210 0 Z"/>
      </g>

      <g class="brand-lockup">
        <circle cx="70" cy="157" r="8" fill="var(--brand-red)"/>
        <text class="wordmark" x="85" y="157" font-size="22">Stonebrook</text>
        <text class="wordmark" x="86" y="173" font-size="10">Putting Institute</text>
      </g>

      <g class="person">
        <text class="person-name" x="568" y="122" text-anchor="end">Pieter de Groenhout</text>
        <text class="person-title" x="568" y="138" text-anchor="end">Director of Golfschool</text>
      </g>

      <g class="address">
        <text x="34" y="226">P.O. Box 48306</text>
        <text x="34" y="242">00452 Nairobi</text>
        <text x="34" y="272"><tspan class="contact-label">C:</tspan> +254 (0) 712408365</text>
        <text x="34" y="288"><tspan class="contact-label">E:</tspan> pieter@stonebrookputt.co.ke</text>
      </g>

      <text class="website" x="566" y="314" text-anchor="end">www.stonebrookputt.com</text>
    </svg>
  </section>

</main>
</body>
</html>
```